company that deals with selling henna and other herbal plant powders needs labels

Hello
the size of the labels is: A6 105 × 148 millimeters.

I need 4 labels each that refers to one of the 4 elements of Nature.
The contents are:
Logo site (florentia vellum)
Name of the grass 1 for each label (Lawsonia Inermis associated with the fire, indigofera tinctoria associated to the air, cassia obovata to the earth, shikakai to the water)
Then it must be inserted:
- Net weight 100 gr.
- Inci (lawsonia inermis, cassia ... etc.)
- vegan, cruelty free, chemical free, preservatives free, No ppd, no ammonia, no peroxide, no pesticides, no synthetic dyes, 100% natural plant dyes, The safe alternative to chemical hair dyes for all hair types
- company name (Quintessa Ltd)

Target Market(s)

Natural beauty product mainly for hair

Colors
acd036
3176b5
33a6d7
faa54b

Requirements
Must have
• Logo site (florentia vellum)
• Net weight 100 gr.
• - Inci (lawsonia inermis, cassia ... etc.)
• - vegan, cruelty free, chemical free, preservatives free, No ppd, no ammonia, no peroxide, no pesticides, no synthetic dyes, 100% natural plant dyes, The safe alternative to chemical hair dyes for all hair types
• - company name (Quintessa Ltd)

```html
<!DOCTYPE html>
<html lang="en">
<head>
<meta charset="utf-8">
<title>Florentia Vellum – Shikakai Label</title>
<link href="https://fonts.googleapis.com/css2?family=Alegreya:wght@500&family=Lato:wght@400;700;900&family=Satisfy&display=swap" rel="stylesheet">
<style>
  :root {
    --backdrop: #d6d6d6;
    --paper: #ffffff;
    --water-top: #52a0cc;
    --water-mid: #8cc1df;
    --water-low: #d9eaf4;
    --water-bottom: #f6fafd;
    --earth-brush: #8a4528;
    --earth-brush-light: #b46d45;
    --ink: #1e1e1e;
    --badge-green: #3f8a2a;
    --badge-green-light: #a6d978;
    --figure-violet: rgba(108, 74, 156, 0.42);
    --figure-blue: rgba(75, 155, 211, 0.40);
    --figure-green: rgba(116, 192, 74, 0.30);
    --mandala-white: rgba(255, 255, 255, 0.22);
  }
  * { box-sizing: border-box; margin: 0; padding: 0; }
  html, body {
    width: 1110px; height: 1200px; overflow: hidden;
    background: var(--backdrop);
  }
  .canvas { position: relative; width: 1110px; height: 1200px; }

  .label {
    position: absolute; left: 145px; top: 22px;
    width: 820px; height: 1156px;
    background: var(--paper);
  }
  .label__field {
    position: absolute; left: 12px; top: 14px; right: 14px; bottom: 20px;
    background: linear-gradient(180deg, var(--water-top) 0%, var(--water-mid) 38%, var(--water-low) 78%, var(--water-bottom) 100%);
    border-radius: 3px;
  }

  .brand-name {
    position: absolute; left: 0; right: 0; top: 164px;
    text-align: center;
    font-family: 'Alegreya', serif; font-weight: 500;
    font-size: 68px; line-height: 80px; color: var(--paper);
    letter-spacing: 0.5px;
  }

  .figure-art {
    position: absolute; left: 170px; top: 258px;
    width: 480px; height: 512px;
    border-radius: 50% 50% 44% 44%;
    background:
      linear-gradient(180deg, var(--figure-green) 0%, var(--figure-blue) 50%, var(--figure-violet) 72%, var(--mandala-white) 100%);
  }

  .product-name {
    position: absolute; left: 126px; top: 768px;
    width: 556px; height: 128px;
    display: flex; align-items: center; justify-content: center;
  }
  .product-name__brush {
    position: absolute; inset: 0;
    background: linear-gradient(180deg, var(--earth-brush) 0%, var(--earth-brush-light) 72%, rgba(180,109,69,0.25) 100%);
    clip-path: polygon(4% 6%, 30% 3%, 55% 6%, 84% 4%, 90% 30%, 100% 46%, 92% 62%, 70% 74%, 40% 90%, 10% 95%, 0% 60%, 3% 30%);
  }
  .product-name__text {
    position: relative;
    font-family: 'Satisfy', cursive; font-size: 54px; line-height: 64px;
    color: var(--paper);
    margin-top: -6px;
  }

  .claims {
    position: absolute; left: 0; right: 0; top: 917px;
    text-align: center; color: var(--ink);
    font-family: 'Lato', sans-serif;
  }
  .claims__list { font-size: 19.5px; line-height: 27px; font-weight: 400; }
  .claims__promise { font-size: 21.5px; line-height: 30px; font-weight: 700; }

  .label__footer {
    position: absolute; left: 0; right: 0; top: 1074px; height: 66px;
  }
  .badge {
    position: absolute; top: 6px; height: 56px;
    display: flex; align-items: center; justify-content: center;
    font-family: 'Lato', sans-serif; font-weight: 700;
    color: var(--badge-green); text-transform: uppercase;
  }
  .badge__shape { position: absolute; inset: 0; width: 100%; height: 100%; }
  .badge__word { position: relative; }
  .badge--vegan { left: 36px; width: 90px; font-size: 22px; }
  .badge--cruelty-free { left: 138px; width: 104px; font-size: 14px; letter-spacing: -0.2px; }

  .maker {
    position: absolute; left: 312px; top: 14px;
    display: flex; align-items: center; gap: 10px;
    font-family: 'Lato', sans-serif; font-weight: 400;
    font-size: 27px; line-height: 40px; color: var(--ink);
  }
  .maker__mark {
    width: 26px; height: 26px; border-radius: 50%;
    background: var(--badge-green);
  }
  .net-weight {
    position: absolute; right: 38px; top: 12px;
    font-family: 'Lato', sans-serif; font-weight: 900;
    font-size: 38px; line-height: 44px; color: var(--ink);
  }
  .net-weight__unit { font-size: 24px; font-weight: 700; }
</style>
</head>
<body>
<div class="canvas">
  <section class="label">
    <div class="label__field"></div>

    <h1 class="brand-name">Florentia Vellum</h1>

    <div class="figure-art" role="img" aria-label="Watercolour illustration of a winged water fairy in a blue and violet petal dress holding a red flower, over a faint white mandala with drops"></div>

    <div class="product-name">
      <div class="product-name__brush" role="img" aria-label="Brown watercolour brush stroke"></div>
      <span class="product-name__text">Shikakai</span>
    </div>

    <div class="claims">
      <p class="claims__list">Chemical Free, Preservatives Free, No Ppd, No Ammonia,<br>No Peroxide, No Pesticides, No Synthetic Dyes</p>
      <p class="claims__promise">100% natural plant dyes.<br>The safe alternative to chemical hair dyes for all hair types</p>
    </div>

    <div class="label__footer">
      <div class="badge badge--vegan">
        <svg class="badge__shape" viewBox="0 0 90 56" aria-hidden="true">
          <path d="M45 54 C10 34 4 18 14 8 C24 -1 38 4 45 14 C52 4 66 -1 76 8 C86 18 80 34 45 54 Z" fill="var(--badge-green-light)"/>
        </svg>
        <span class="badge__word">Vegan</span>
      </div>
      <div class="badge badge--cruelty-free">
        <svg class="badge__shape" viewBox="0 0 104 56" aria-hidden="true">
          <circle cx="52" cy="28" r="27" fill="var(--badge-green-light)"/>
        </svg>
        <span class="badge__word">Cruelty Free</span>
      </div>
      <div class="maker">
        <span class="maker__mark"></span>
        <span class="maker__name">Quintessa Ltd</span>
      </div>
      <div class="net-weight">100 <span class="net-weight__unit">Gr</span></div>
    </div>
  </section>
</div>
</body>
</html>
```